Brindle and Fern LLC | Land Clearing, Landscaping & Dump Trailer Services

Project Description: Brindle and Fern LLC Website Design
The website will be published using squarespace
Objective:
Design a visually compelling and conversion-driven website for Brindle and Fern LLC, a land solutions business based in Pickens County, Georgia. The site will highlight the company’s professionalism, locally rooted service, and commitment to quality in land clearing, grading, and dump trailer services.
Pages & Features to Include:
1. Landing Page (Homepage)
- Clear tagline: Sculpting Land with Precision and Power
- Call-to-Action (CTA) buttons: “Get a Free Quote” and “View Services”
- Service highlights with icons or photos (e.g., grading, mulching, hauling)
- Customer testimonials
- Embedded contact form
- Google Maps integration showing service area
2. Services + Pricing Page
- Organized list of services under 3 categories:
- **Land Clearing & Grading**
- Forestry Mulching
- Gravel Driveway Repair
- Minimum Job Fee:
- Dump Trailer Services
- Trailer Rental (Daily):
- Junk Removal (Full Load)
- Material Delivery: $ + mileage
- Specialty Jobs
- Stump removal, light demolition
- Each service section includes short descriptions and photos
- Optional quote form at the bottom with “Request a Quote” CTA
Design Style:
- Clean, professional design using clean tones
- Fonts that balance industrial strength and local charm
- Mobile-optimized with fast loading speeds and easy navigation
- SEO-optimized for terms like *land clearing Pickens County*, *grading services North Georgia*, and *dump trailer rental Jasper GA*, etc...

```html
<!DOCTYPE html>
<html lang="en">
<head>
<meta charset="utf-8">
<title>Brindle and Fern LLC | Land Clearing, Grading &amp; Dump Trailer Services</title>
<link href="https://fonts.googleapis.com/css2?family=Krona+One&family=Roboto:wght@400;500;700&family=Roboto+Condensed:wght@500;700&display=swap" rel="stylesheet">
<style>
:root{
  --green:#4b8f2c;
  --green-dark:#3f7a24;
  --ink:#222;
  --charcoal:#333;
  --slate:#474747;
  --night:#1c1c1c;
  --deep:#121212;
  --mist:#e7e7e7;
  --paper:#fff;
  --muted:#666;
  --display:"Krona One",sans-serif;
  --body:"Roboto",sans-serif;
  --cond:"Roboto Condensed",sans-serif;
}
*{box-sizing:border-box;margin:0;padding:0}
html,body{width:1200px;height:3873px;overflow:hidden}
body{position:relative;font-family:var(--body);color:var(--ink);background:var(--paper)}
.abs{position:absolute}

/* header */
.brand{left:105px;top:32px;font:700 16px var(--body);color:var(--ink);display:flex;align-items:center;gap:8px}
.brand-square{width:18px;height:18px;background:var(--green)}
.topbar-address{left:560px;top:0;width:370px;height:26px;background:var(--charcoal);clip-path:polygon(4% 0,100% 0,96% 100%,0 100%);color:#fff;font-size:15px;display:flex;align-items:center;justify-content:center;gap:6px}
.topbar-social{left:910px;top:0;width:290px;height:26px;background:var(--green);clip-path:polygon(0 0,100% 0,100% 100%,5% 100%);display:flex;align-items:center;justify-content:center;gap:24px}
.dot{width:12px;height:12px;border-radius:50%;background:#fff}
.nav{top:52px;left:573px;display:flex;gap:58px;font-size:16px}
.nav a{color:var(--ink);text-decoration:none}
.nav a::after{content:"";display:inline-block;width:5px;height:5px;background:var(--ink);margin-left:6px;vertical-align:middle}
.nav a.active{color:var(--green)}
.nav a.active::after{background:var(--green)}
.phone-badge{left:928px;top:44px;width:36px;height:36px;border-radius:50%;background:var(--green);display:flex;align-items:center;justify-content:center}
.phone-text{left:974px;top:43px;font-size:13px;color:#444}
.phone-text b{display:block;font:700 19px var(--body);color:var(--ink);margin-top:3px}

/* hero */
.hero{left:0;top:90px;width:1200px;height:567px;background:linear-gradient(100deg,#5a5a5a 0%,#2d2d2d 45%,#3b3b3b 75%,#555 100%)}
.hero-title{left:525px;top:310px;font:400 43px/56px var(--display);color:#fff;letter-spacing:1px;white-space:nowrap}
.btn{display:flex;align-items:center;justify-content:center;font:700 17px var(--body);color:#fff;border-radius:4px}
.btn-green{background:var(--green)}
.btn-outline{border:2px solid #fff;font-weight:500}

/* section headings */
.heading{left:0;width:1200px;text-align:center;font:400 32px var(--display);color:var(--ink);letter-spacing:1px}
.rule{width:60px;height:4px;background:var(--green);left:570px}

/* service cards */
.service{width:310px;height:435px;top:826px;background:#e9e9e9;border:1px solid #ddd;border-radius:4px;overflow:hidden}
.service.dark{background:var(--charcoal);color:#fff}
.service-photo{position:absolute;left:0;top:0;width:310px;height:360px;clip-path:polygon(0 0,100% 0,100% 100%,0 70%)}
.service-icon{position:absolute;left:24px;top:240px;width:54px;height:54px;border-radius:50%;background:var(--green);border:3px solid #fff;display:flex;align-items:center;justify-content:center}
.service h3{position:absolute;left:28px;top:316px;font:700 28px var(--cond)}
.service p{position:absolute;left:28px;top:355px;width:250px;font-size:13px;line-height:19px;color:#555}
.service.dark p{color:#ddd}
.service .link{position:absolute;left:28px;top:397px;font:700 15px var(--body);text-decoration:underline}

/* testimonials */
.testimonials{left:0;top:1519px;width:1200px;height:597px;background:var(--mist)}
.review{top:1680px;width:310px;height:327px;background:#fff;border-radius:4px;overflow:hidden}
.review.featured{background:var(--green);color:#fff}
.review-corner{position:absolute;left:0;top:0;width:310px;height:52px;background:var(--green);clip-path:polygon(0 0,100% 0,0 100%)}
.review.featured .review-corner{background:var(--charcoal)}
.avatar{position:absolute;left:18px;top:22px;width:70px;height:70px;border-radius:50%;background:#cfc5bb;border:3px solid #fff}
.review h4{position:absolute;left:105px;top:36px;font:500 17px var(--body);white-space:nowrap}
.review .role{position:absolute;left:105px;top:60px;font-size:13px}
.stars{position:absolute;left:105px;top:79px;color:#e33;font-size:13px;letter-spacing:1px}
.review.featured .stars{color:#fff}
.review blockquote{position:absolute;left:21px;top:127px;width:270px;font-size:14px;line-height:22.5px;color:#555}
.review.featured blockquote{color:#fff}
.quote-mark{position:absolute;right:16px;bottom:4px;font:700 60px/1 Georgia,serif;color:#ddd}
.review.featured .quote-mark{color:rgba(255,255,255,.35)}

/* quote */
.quote-section{left:0;top:2116px;width:1200px;height:678px;background:var(--slate)}
.quote-brand{left:80px;top:2420px;width:440px;font:700 44px/54px var(--body);color:#fff}
.quote-frame{left:520px;top:2256px;width:572px;height:478px;border:6px solid var(--green);clip-path:polygon(0 0,28% 0,28% 6px,6px 6px,6px 100%,0 100%,0 0,100% 0,100% 100%,72% 100%,72% calc(100% - 6px),100% calc(100% - 6px))}
.quote-card{left:526px;top:2262px;width:564px;height:466px;background:var(--charcoal)}
.quote-card h2{position:absolute;left:31px;top:36px;font:400 30px var(--display);color:#fff;letter-spacing:1px}
.field-label{position:absolute;font:700 12px var(--body);color:#fff}
.field{position:absolute;height:35px;background:#fff;border:1px solid #ccc;font-size:12px;color:#555;padding:10px 8px}
.field-select{display:flex;justify-content:space-between;align-items:center;padding:0 8px}

/* area */
.area-band{left:0;top:2794px;width:1200px;height:146px;background:var(--green)}
.area-band h2{position:absolute;left:0;width:1200px;top:50px;text-align:center;font:400 34px var(--display);color:#fff;letter-spacing:1px}
.area-band .rule{background:#fff;top:100px}
.map{left:0;top:2940px;width:1200px;height:520px;background:linear-gradient(160deg,#f1f1f1,#e2e2e2)}

/* footer */
.footer{left:0;top:3459px;width:1200px;height:351px;background:var(--night)}
.f-title{font:700 15px var(--body);color:#fff}
.f-text{font-size:13px;line-height:19px;color:#ddd}
.f-icon{width:28px;height:28px;border-radius:50%;background:var(--green);display:flex;align-items:center;justify-content:center}
.newsletter{left:787px;top:3632px;width:296px;height:50px;background:#fff;display:flex;align-items:center;padding-left:18px;font-size:16px;color:#333}
.newsletter-btn{position:absolute;right:0;top:0;width:66px;height:50px;background:var(--green);clip-path:polygon(12% 0,100% 0,100% 100%,0 100%);display:flex;align-items:center;justify-content:center}
.bottom-bar{left:0;top:3810px;width:1200px;height:63px;background:var(--deep)}
.bottom-right{left:610px;top:3810px;width:590px;height:63px;background:#262626;clip-path:polygon(8% 0,100% 0,100% 100%,0 100%)}
.social-circle{width:28px;height:28px;border-radius:50%;background:var(--green)}
</style>
</head>
<body>

<header>
  <div class="abs brand"><span class="brand-square"></span>Brindle and Fern LLC</div>
  <div class="abs topbar-address">
    <svg width="12" height="14" viewBox="0 0 12 14"><path d="M6 0a5 5 0 0 0-5 5c0 4 5 9 5 9s5-5 5-9a5 5 0 0 0-5-5zm0 7a2 2 0 1 1 0-4 2 2 0 0 1 0 4z" fill="#fff"/></svg>
    418 Ridgeline Rd, Jasper GA 30143
  </div>
  <div class="abs topbar-social"><span class="dot"></span><span class="dot"></span><span class="dot"></span><span class="dot"></span></div>
  <nav class="abs nav"><a class="active">Home</a><a>Services</a><a>Contact</a></nav>
  <div class="abs phone-badge"><svg width="16" height="16" viewBox="0 0 24 24"><path d="M6.6 10.8a15 15 0 0 0 6.6 6.6l2.2-2.2a1 1 0 0 1 1-.25 11.4 11.4 0 0 0 3.6.57 1 1 0 0 1 1 1V20a1 1 0 0 1-1 1A17 17 0 0 1 3 4a1 1 0 0 1 1-1h3.5a1 1 0 0 1 1 1c0 1.25.2 2.45.57 3.57a1 1 0 0 1-.25 1z" fill="#fff"/></svg></div>
  <div class="abs phone-text">Toll Free Number<b>555-014-2290</b></div>
</header>

<section>
  <div class="abs hero" role="img" aria-label="Black and white photo of a skid steer loader working on a job site"></div>
  <h1 class="abs hero-title">SCULPTING LAND<br>WITH PRECISION<br>AND POWER</h1>
  <a class="abs btn btn-green" style="left:527px;top:491px;width:190px;height:55px">GET A FREE QUOTE</a>
  <a class="abs btn btn-outline" style="left:731px;top:491px;width:190px;height:55px">VIEW SERVICES</a>
</section>

<section>
  <h2 class="abs heading" style="top:740px">OUR SERVICES</h2>
  <div class="abs rule" style="top:786px"></div>

  <article class="abs service" style="left:105px">
    <div class="service-photo" role="img" aria-label="Forestry mulcher clearing trees in a pine forest" style="background:linear-gradient(180deg,#9a9a9a,#4f4f4f)"></div>
    <div class="service-icon"><svg width="26" height="26" viewBox="0 0 24 24"><circle cx="12" cy="12" r="9" fill="none" stroke="#fff" stroke-width="2"/><path d="M3 12h18M12 3c3 3 3 15 0 18M12 3c-3 3-3 15 0 18" stroke="#fff" stroke-width="1.5" fill="none"/></svg></div>
    <h3>Land Clearing</h3>
    <p>Lorem Ipsum has been the industry's standard dummy</p>
    <a class="link">GET A QUOTE</a>
  </article>

  <article class="abs service dark" style="left:445px">
    <div class="service-photo" role="img" aria-label="Worker in ear protection operating orange grading equipment" style="background:linear-gradient(160deg,#6d6f80,#3a3f52 55%,#c0602a)"></div>
    <div class="service-icon"><svg width="26" height="26" viewBox="0 0 24 24"><path d="M3 8h11l3 6H7z" fill="#fff"/><circle cx="8" cy="18" r="2.5" fill="#fff"/><path d="M17 14l4-6" stroke="#fff" stroke-width="2"/></svg></div>
    <h3>Land Grading</h3>
    <p>Lorem Ipsum has been the industry's standard dummy</p>
    <a class="link">GET A QUOTE</a>
  </article>

  <article class="abs service" style="left:780px">
    <div class="service-photo" role="img" aria-label="Dump trailer being loaded beside a white truck" style="background:linear-gradient(180deg,#b8b8b8,#555)"></div>
    <div class="service-icon"><svg width="28" height="24" viewBox="0 0 28 24"><rect x="2" y="6" width="15" height="10" fill="#fff"/><path d="M18 9h5l3 4v3h-8z" fill="#fff"/><circle cx="7" cy="18" r="2.5" fill="#fff"/><circle cx="21" cy="18" r="2.5" fill="#fff"/></svg></div>
    <h3>Dump Trailer</h3>
    <p>Lorem Ipsum has been the industry's standard dummy</p>
    <a class="link">GET A QUOTE</a>
  </article>

  <a class="abs btn btn-green" style="left:505px;top:1291px;width:190px;height:56px;font-size:16px">VIEW ALL SERVICES</a>
</section>

<section>
  <div class="abs testimonials"></div>
  <h2 class="abs heading" style="top:1588px">CLIENT TESTIMONIAL</h2>
  <div class="abs rule" style="top:1636px"></div>
  <svg class="abs" style="left:64px;top:1806px" width="16" height="24" viewBox="0 0 16 24"><path d="M12 3 4 12l8 9" stroke="#777" stroke-width="3" fill="none"/></svg>
  <svg class="abs" style="left:1112px;top:1806px" width="16" height="24" viewBox="0 0 16 24"><path d="M4 3l8 9-8 9" stroke="var(--green)" stroke-width="3" fill="none"/></svg>

  <article class="abs review" style="left:105px">
    <div class="review-corner"></div>
    <div class="avatar" role="img" aria-label="Customer portrait"></div>
    <h4>MARCUS HALE</h4><span class="role">Our Customer</span><span class="stars">★★★★★</span>
    <blockquote>“ Lorem Ipsum has been the industry's standard dummy text ever since the 1500s, when an unknown printer took a galley of type and scrambled it to make a type specimen book. ”</blockquote>
    <span class="quote-mark">❞</span>
  </article>

  <article class="abs review featured" style="left:445px">
    <div class="review-corner"></div>
    <div class="avatar" role="img" aria-label="Customer portrait"></div>
    <h4>DEAN PORTER</h4><span class="role">Our Customer</span><span class="stars">★★★★★</span>
    <blockquote>“ Lorem Ipsum has been the industry's standard dummy text ever since the 1500s, when an unknown printer took a galley of type and scrambled it to make a type specimen book. ”</blockquote>
    <span class="quote-mark">❞</span>
  </article>

  <article class="abs review" style="left:784px">
    <div class="review-corner"></div>
    <div class="avatar" role="img" aria-label="Customer portrait"></div>
    <h4>CLARA WHITFIELD</h4><span class="role">Our Customer</span><span class="stars">★★★★★</span>
    <blockquote>“ Lorem Ipsum has been the industry's standard dummy text ever since the 1500s, when an unknown printer took a galley of type and scrambled it to make a type specimen book. ”</blockquote>
    <span class="quote-mark">❞</span>
  </article>
</section>

<section>
  <div class="abs quote-section"></div>
  <div class="abs quote-brand">Brindle and Fern LLC</div>
  <div class="abs quote-frame"></div>
  <form class="abs quote-card">
    <h2>GET A QUOTE</h2>
    <span class="field-label" style="left:32px;top:96px">NAME</span>
    <div class="field" style="left:32px;top:111px;width:232px">Your First &amp; Last Name</div>
    <span class="field-label" style="left:290px;top:96px">EMAIL</span>
    <div class="field" style="left:290px;top:111px;width:232px">Example@gmail.com</div>
    <span class="field-label" style="left:32px;top:174px">PHONE</span>
    <div class="field" style="left:32px;top:189px;width:232px">+1</div>
    <span class="field-label" style="left:290px;top:174px">SERVICES</span>
    <div class="field field-select" style="left:290px;top:189px;width:232px">Which service do you need?<svg width="10" height="6" viewBox="0 0 10 6"><path d="M1 1l4 4 4-4" stroke="#222" stroke-width="1.6" fill="none"/></svg></div>
    <span class="field-label" style="left:32px;top:246px">MESSAGE</span>
    <div class="field" style="left:32px;top:261px;width:490px;height:100px">Tell us what you'd like to talk to us about</div>
    <a class="btn btn-green" style="position:absolute;left:31px;top:376px;width:182px;height:52px;font-size:16px">SUBMIT NOW</a>
  </form>
</section>

<section>
  <div class="abs area-band">
    <h2>OUR SERVICES AREA</h2>
    <div class="abs rule"></div>
  </div>
  <div class="abs map" role="img" aria-label="Map of the service area with location markers"></div>
  <svg class="abs" style="left:0;top:3360px" width="1200" height="100" viewBox="0 0 1200 100"><polygon points="0,100 600,2 1200,82 1200,100" fill="var(--night)"/></svg>
</section>

<footer>
  <div class="abs footer"></div>
  <div class="abs brand" style="top:3562px;color:#fff"><span class="brand-square"></span>Brindle and Fern LLC</div>
  <p class="abs f-text" style="left:108px;top:3622px;width:180px">Lorem Ipsum has been the industry's standard dummy text ever since the 1500s</p>

  <h4 class="abs f-title" style="left:337px;top:3520px">QUICK SERVICES</h4>
  <div class="abs f-icon" style="left:337px;top:3582px"><svg width="14" height="14" viewBox="0 0 24 24"><path d="M12 3 2 12h3v8h5v-5h4v5h5v-8h3z" fill="#fff"/></svg></div>
  <p class="abs f-text" style="left:380px;top:3572px">Address :<br><span style="color:#fff">418 Ridgeline Rd, Jasper GA 30143</span></p>
  <div class="abs f-icon" style="left:337px;top:3641px"><svg width="14" height="12" viewBox="0 0 24 20"><rect x="1" y="2" width="22" height="16" fill="#fff"/><path d="M1 2l11 9 11-9" stroke="var(--green)" stroke-width="2" fill="none"/></svg></div>
  <p class="abs f-text" style="left:383px;top:3633px">Email :<br><b style="color:#fff">hello@brindlefern.com</b></p>

  <h4 class="abs f-title" style="left:605px;top:3520px">QUICK SERVICES</h4>
  <p class="abs f-text" style="left:605px;top:3574px;line-height:32px">Land clearing<br>Land grading<br>Dump trailer</p>

  <h4 class="abs f-title" style="left:787px;top:3520px">SIGN UP NEWSLETTER</h4>
  <p class="abs f-text" style="left:787px;top:3572px;font-size:14px;line-height:25px">Subscribe Our Newsletter To Get Our<br>latest updates &amp; news</p>
  <div class="abs newsletter">Instant Quote
    <span class="newsletter-btn"><svg width="18" height="18" viewBox="0 0 24 24"><path d="M2 12 22 3l-6 18-4-7z" fill="#222"/></svg></span>
  </div>

  <div class="abs bottom-bar"></div>
  <div class="abs bottom-right"></div>
  <p class="abs f-text" style="left:108px;top:3834px;color:#fff">Copyright © 2025 <span style="color:var(--green)">Brindle and Fern LLC</span>, ALL RIGHT RESEVED</p>
  <p class="abs f-title" style="left:638px;top:3834px;font-size:14px">FOLLOW US ON SOCIAL MEDIA :</p>
  <div class="abs" style="left:956px;top:3826px;display:flex;gap:9px"><span class="social-circle"></span><span class="social-circle"></span><span class="social-circle"></span><span class="social-circle"></span></div>
</footer>

</body>
</html>
```